Ashworth Web Design Project

I need the front page and an internal page designed for this client's website. The logo is attached. Obviously the colors have to go with and/or work with the logo colors. I also attached a very rough brochure layout to help you see the direction we're going in with print materials. The rough site map is also attached. I see a slider on the homepage, the art for which I may come back to you to create. This clinic is in a very high end Dallas neighborhood. The hook is that it's a primary care and urgent facility with convenient hours.

I don't know how much this impacts your design, but this will be a Wordpress site and I'm using a framework called Struxo (struxo-demo.example). If Struxo proves to be inflexible, I'll have to get a template that allows me to execute your design.

This site (http://oakbendcareclinic.example) has the type and quality of content I will eventually have on the Ashworth site.

I just revised the brief for this project. I added the site map and added details to the overview and the "Must Have" section. Thank you for revisiting the brief. 

Reason: Christmas was a bad time to end it.

Target Market(s)

Women 25-54 with children living at home, income over $150k/year

Industry/Entity Type

Clinic

Requirements
Must have
• Masthead incorporating the logo
Followed by the primary nav
Slider on the home page below that
Dual nav - 1 with the nav in the attached site map
2 secondary nav with areas of healthcare
There will three blocks under the nav
1. It's about time (with a small blurb less than 50 words.
2. It's about choices (with small blurb)
3. It's about you (with small blurb)
Three footer blocks
patient check in link on every page
"No appointment? No problem" icon on every page

```html
<!DOCTYPE html>
<html lang="en">
<head>
<meta charset="utf-8">
<title>Ashworth Medical</title>
<link href="https://fonts.googleapis.com/css2?family=Ubuntu:wght@400;500;700&family=Open+Sans:wght@400;600;700&display=swap" rel="stylesheet">
<style>
:root{
  --green:#1ccf67;
  --green-dark:#0f9e48;
  --blue:#0f6fc0;
  --blue-dark:#0a4f96;
  --blue-text:#1b6aad;
  --ink:#333;
  --rule:#c8c8c8;
  --slide:#b9c6bd;
  --slide-low:#a6b5aa;
}
*{box-sizing:border-box;margin:0;padding:0}
html,body{width:1029px;height:1200px;overflow:hidden}
body{position:relative;background:#fff;font-family:"Open Sans",Arial,sans-serif;color:var(--ink)}
.abs{position:absolute}
.masthead{left:0;top:0;width:1029px;height:133px;background:linear-gradient(#fff,#ececec)}
.brand{left:88px;top:32px;display:flex;align-items:center;gap:8px}
.brand-dot{width:38px;height:38px;border-radius:50%;background:var(--blue)}
.brand-name{font-family:"Ubuntu",sans-serif;font-weight:700;font-size:25px;color:var(--blue);line-height:1}
.brand-tag{font-size:8px;color:#444;margin-top:2px}
.phone{right:89px;top:16px;display:flex;align-items:center;gap:8px;font-family:"Ubuntu",sans-serif;font-size:20px;font-weight:500;color:#444;letter-spacing:1px}
.follow{right:88px;top:72px;display:flex;align-items:center;gap:12px;font-family:"Ubuntu",sans-serif;font-size:15px;color:#444}
.social{width:27px;height:27px;border-radius:50%;background:linear-gradient(#5aa0e0,#1d5fae)}
.social.tw{background:linear-gradient(#b7eef0,#5cc4d0)}
.hero{left:0;top:133px;width:1029px;height:354px;background:linear-gradient(#22d86f,#13b552 60%,#0f9e48)}
.nav{left:87px;top:114px;width:855px;height:36px;border-radius:6px;background:linear-gradient(#1a84d6,#0a55a3);border:1px solid #fff;display:flex;overflow:hidden}
.nav a{color:#fff;text-decoration:none;font-size:12px;font-family:Arial,sans-serif;display:flex;align-items:center;justify-content:center;border-right:1px solid #2d6fb0}
.nav a:last-child{border-right:0}
.nav a.current{background:linear-gradient(#28d16e,#109a47)}
.slide{border:4px solid #fff;box-shadow:0 8px 10px rgba(0,0,0,.25);background:linear-gradient(var(--slide),var(--slide-low))}
.slide.side{top:215px;height:203px}
.arrow{width:34px;height:34px;border-radius:50%;background:radial-gradient(#3fe189,#15a24f);border:2px solid #8fe8b5;top:301px}
.btn{border-radius:10px;color:#fff;font-family:"Ubuntu",sans-serif;font-weight:700}
.btn-appt{left:87px;top:521px;width:188px;height:59px;background:linear-gradient(#2ee07d,#0f9e48);display:flex;align-items:center;gap:10px;padding-left:9px;font-size:13.5px;line-height:1.35}
.appt-card{width:41px;height:32px;background:#d9382b;border:2px solid #fff;transform:rotate(-6deg)}
.btn-check{left:89px;top:599px;width:188px;height:59px;background:linear-gradient(#2790e2,#0a55a3)}
.avatar{left:14px;top:4px;width:42px;height:50px;border-radius:21px 21px 8px 8px;background:linear-gradient(#fff,#c9ced4)}
.card{top:521px;width:199px;height:140px;background:linear-gradient(#fbfbfb,#ececec);border-radius:8px;padding:12px 14px}
.card h3{font-family:"Ubuntu",sans-serif;font-weight:400;font-size:15.5px;color:var(--blue-text);display:flex;align-items:center;gap:7px;margin-bottom:14px}
.card h3 b{font-weight:500;color:#333}
.mark{width:24px;height:24px;border-radius:50%;background:var(--blue);flex:none}
.card p{font-size:9.6px;line-height:15.5px;text-align:justify;color:#333}
.more{position:absolute;right:13px;bottom:10px;font-size:9.6px;font-weight:700;color:var(--blue-text)}
.card ul{list-style:none;font-size:10.6px;line-height:19px;color:#333}
.card li::before{content:"";display:inline-block;border-left:4px solid var(--blue);border-top:3px solid transparent;border-bottom:3px solid transparent;margin:0 10px 1px 2px}
.sidenav{left:94px;top:684px;width:183px;height:287px;background:linear-gradient(90deg,#f7f7f7,#efefef);border-radius:10px}
.sidenav ul{list-style:none;position:absolute;left:7px;top:24px;width:155px}
.sidenav li{height:31px;display:flex;align-items:center;font-size:11.3px;font-family:Arial,sans-serif;color:#333;border-bottom:1px dashed var(--rule);white-space:nowrap}
.sidenav li span{font-size:9px;font-weight:700;margin-right:9px}
.sidenav li.current{margin-left:-15px;padding-left:15px;width:178px;background:var(--blue-dark);color:#fff;border:0;clip-path:polygon(0 0,90% 0,100% 50%,90% 100%,0 100%)}
.main{left:311px;top:700px;width:600px}
.main h2{font-family:"Ubuntu",sans-serif;font-weight:400;font-size:21px;color:var(--blue-text);display:flex;align-items:center;gap:9px;margin-bottom:10px}
.lead{font-size:9.6px;font-weight:700;line-height:17px}
.partners{font-size:10.6px;font-weight:700;color:#17b856;margin:9px 0 22px}
.main ul{list-style:none;font-size:9.8px;line-height:17.2px;padding-left:18px}
.main li::before{content:"";display:inline-block;border-left:4px solid var(--blue);border-top:3px solid transparent;border-bottom:3px solid transparent;margin:0 10px 1px 0}
.cta{font-size:11px;font-weight:600;margin-top:14px}
.footnav{left:0;top:990px;width:1029px;height:37px;background:var(--green-dark);display:flex;align-items:center;padding-left:94px;gap:13px;font-size:11.7px;color:#fff;font-family:Arial,sans-serif}
.footer{left:0;top:1027px;width:1029px;height:173px;background:linear-gradient(#0f73c8,#0b4f97)}
.up{left:894px;top:984px;width:50px;height:50px;border-radius:50%;background:linear-gradient(#7af0ee,#22c3d3);color:#fff;font-size:10px;font-weight:700;display:flex;align-items:center;justify-content:center}
.fbrand{left:104px;top:1066px;display:flex;align-items:center;gap:8px;color:#fff}
.fbrand .brand-dot{background:#6aa6e0}
.fbrand .brand-name{color:#fff}
.fbrand .brand-tag{color:#dde}
.copy{left:107px;top:1154px;color:#fff;font-size:10.2px;font-weight:700;line-height:17px}
.testimonial{left:408px;top:1042px;width:259px;height:127px;border-radius:14px;background:linear-gradient(#24dc74,#12b650);padding:9px 15px;color:#fff}
.testimonial h4{font-family:"Ubuntu",sans-serif;font-size:17px;font-weight:700;margin-bottom:6px}
.testimonial p{font-size:8.6px;line-height:15.4px;text-align:justify}
.author{left:451px;top:1180px;color:#fff;font-size:9.5px}
.contact{left:739px;top:1046px;color:#fff}
.contact h4{font-family:"Ubuntu",sans-serif;font-size:17px;font-weight:700;margin-bottom:6px}
.contact p{font-size:9.8px;line-height:14px}
.fsocial{left:741px;top:1124px;display:flex;gap:15px}
.fsocial i{width:27px;height:27px;border-radius:50%;background:#fff;opacity:.85}
.legal{right:90px;top:1173px;color:#fff;font-size:10.6px;font-weight:700}
</style>
</head>
<body>
<header class="abs masthead"></header>
<div class="abs brand"><span class="brand-dot"></span><div><div class="brand-name">AshworthMedical</div><div class="brand-tag">Immediate Family and Personal Care</div></div></div>
<div class="abs phone"><svg width="20" height="20" viewBox="0 0 20 20"><rect width="20" height="20" rx="3" fill="#18b04f"/><path d="M6 4c1 0 2 3 1.5 3.5S6.5 9 8 11.5 11 13 11.5 12.5 15 13 15 14s-2 2-3 2C8 15.5 4.5 12 4 8c0-1 1-4 2-4z" fill="#fff"/></svg>(555) 214 7720</div>
<div class="abs follow">Follow Us On <span class="social"></span><span class="social"></span><span class="social tw"></span></div>

<section class="abs hero"></section>
<nav class="abs nav">
  <a class="current" style="width:78px">Home</a><a style="width:111px">About us</a><a style="width:173px">Health Care Services</a><a style="width:156px">Patient Resources</a><a style="width:138px">Appointments</a><a style="width:90px">Blog</a><a style="width:109px">Contact</a>
</nav>
<div class="abs arrow" style="left:93px"></div>
<div class="abs arrow" style="left:904px"></div>
<div class="abs slide side" role="img" aria-label="Photo of a family relaxing on grass with their dog" style="left:133px;width:180px"></div>
<div class="abs slide side" role="img" aria-label="Photo of a father and child running on a lawn" style="left:716px;width:187px"></div>
<div class="abs slide" role="img" aria-label="Photo of a family walking hand in hand across a garden" style="left:310px;top:185px;width:409px;height:273px"></div>

<a class="abs btn btn-appt"><span class="appt-card"></span><span>No Appointment?<br>No Problem</span></a>
<a class="abs btn btn-check"><span class="abs avatar"></span><span class="abs" style="left:68px;top:8px;font-size:15px">Patient Check</span><span class="abs" style="left:113px;top:35px;font-size:11px;font-weight:400;font-style:italic;text-decoration:underline;font-family:Arial,sans-serif">Click Here</span></a>

<article class="abs card" style="left:306px"><h3><span class="mark"></span><span>About <b>Company</b></span></h3><p>Lorem Ipsum is simply dummy text of the printing and typesetting industry. Lorem Ipsum has been the industry's standard dummy text...</p><span class="more">More Info [+]</span></article>
<article class="abs card" style="left:524px"><h3><span class="mark"></span><span>Family <b>Medicine</b></span></h3><p>Lorem Ipsum is simply dummy text of the printing and typesetting industry. Lorem Ipsum has been the industry's standard dummy text...</p><span class="more">More Info [+]</span></article>
<article class="abs card" style="left:743px"><h3><span class="mark"></span><span>Our <b>Clinic</b></span></h3><ul><li>Family Medicine</li><li>Immediate Statement</li><li>Travel Medicine</li><li>On-Site Laboratory Services</li></ul></article>

<aside class="abs sidenav"><ul>
  <li class="current"><span>[+]</span>Routine Health Care</li>
  <li><span>[+]</span>Our Staff</li>
  <li><span>[+]</span>Location &amp; Contact Info</li>
  <li><span>[+]</span>Appointments &amp; Office Hours</li>
  <li><span>[+]</span>Walk-Ins</li>
  <li><span>[+]</span>Day of Appointment</li>
  <li><span>[+]</span>Missed &amp; Late Appointments</li>
  <li><span>[+]</span>Prescriptions &amp; Product</li>
</ul></aside>

<main class="abs main">
  <h2><span class="mark"></span>Health Care Services</h2>
  <p class="lead">Ashworth medical Clinic is a medical practice that provides quality family health care as well as timely immediate care for acute illness or injury.</p>
  <p class="partners">Businesses who have partnered with AFM:</p>
  <ul>
    <li>Patient Consent and Financial Disclosure</li>
    <li>Authorization to Release/Obtain Medical Records</li>
    <li>HIPAA Consent Form</li>
    <li>Minor Consent Form</li>
    <li>Health History</li>
    <li>Patient Information Sheet</li>
    <li>Northvale School District: Health Services Forms</li>
  </ul>
  <p class="cta">What are you waiting for? Call us NOW on 02 5550 1834. We will exceed your expectations.</p>
</main>

<nav class="abs footnav"><span>Home</span>~<span>About us</span>~<span>Health Care Services</span>~<span>Patient Resources</span>~<span>Appointments</span>~<span>Blog</span>~<span>Contact</span></nav>
<footer class="abs footer"></footer>
<div class="abs up">UP</div>
<div class="abs fbrand"><span class="brand-dot"></span><div><div class="brand-name">AshworthMedical</div><div class="brand-tag">Immediate Family and Personal Care</div></div></div>
<p class="abs copy">© Copyright 2006-2011 Ashworth Medical<br>All Rights Reserved</p>
<section class="abs testimonial"><h4>Testimonial</h4><p>Lorem Ipsum is simply dummy text of the printing and typesetting industry. Lorem Ipsum has been the industry's standard dummy text ever since the 1500s, when an unknown printer took a galley of type and scrambled</p></section>
<svg class="abs" style="left:600px;top:1166px" width="24" height="16" viewBox="0 0 24 16"><path d="M0 0h24L14 16z" fill="#12b650"/></svg>
<p class="abs author">Marlon Tedesco, Fairbrook, NH</p>
<section class="abs contact"><h4>Get in touch</h4><p>AshworthFamilymedical.example<br>4120 Ashworth Ave (at Elm Row) Ste 210,<br>Dallas , tX75000</p></section>
<div class="abs fsocial"><i></i><i></i><i></i><i></i><i></i></div>
<p class="abs legal">Terms &amp; Conditions &nbsp;|&nbsp; Privacy Policy</p>
</body>
</html>
```